Movrette Business Card

We need a business card design for Movrette, an independent sewing pattern company based near Quebec City. We make patterns for children and adults and specialize in everything other big pattern brands won't tackle: activewear, sportswear (figure skating, gymnastics), underwear. We are a small business and would like our cards to be stylish and fun, not corporate looking.

Target Market(s)

Educated women 35-55 who sew for themselves or their family. They like fashion and sew to be different and make clothes that fit them like a glove, not necessarily to save money.

Industry/Entity Type

Small Business

Requirements
Must have
• Movrette logo, contact info:

Odile Parmont, president & founder / présidente et fondatrice

Movrette
3915 rue Lavoie
St-Aubrevin QC H2K4P8
Canada

info@movrette.com
www.movrette.com
Nice to have
• Sewing/fashion-related graphics. You can use any pattern cover available on www.movrette.com for inspiration. Stylish illustrations / sketches inspired by existing garments we have would be great. Something showing pattern grading could also be an option.

The design can be on one- or two-sided. We are open to variations (e.g. 4-5 different backs for a given card)
Should not have
• nothing too cartoonish or girly please :) we prefer something timeless, fashion-forward.

```html
<!DOCTYPE html>
<html lang="en">
<head>
<meta charset="utf-8">
<title>Movrette Business Card</title>
<link rel="stylesheet" href="https://fonts.googleapis.com/css2?family=Open+Sans:wght@400;600;700&display=swap">
<style>
  :root {
    --stage: #2b2b2d;
    --card-black-top: #2a2a2a;
    --card-black-bottom: #050505;
    --card-white: #f2f2f2;
    --card-white-shade: #dcdcdc;
    --ink: #111111;
    --paper: #ffffff;
    --swoosh: #c9c9c9;
    --swoosh-light: #e6e6e6;
  }
  * { margin: 0; padding: 0; box-sizing: border-box; }
  html, body {
    width: 1200px;
    height: 900px;
    overflow: hidden;
    background: var(--stage);
    font-family: "Open Sans", Arial, sans-serif;
  }
  .canvas {
    position: relative;
    width: 1200px;
    height: 900px;
  }
  .card {
    position: absolute;
    width: 540px;
    height: 310px;
    border-radius: 26px;
    overflow: hidden;
    box-shadow: 0 14px 30px rgba(0,0,0,0.45);
  }
  .card-front {
    left: 110px;
    top: 130px;
    background: linear-gradient(180deg, var(--card-black-top) 0%, var(--card-black-bottom) 100%);
  }
  .front-name {
    position: absolute;
    left: 38px;
    top: 48px;
    font-size: 96px;
    font-weight: 700;
    color: var(--paper);
    letter-spacing: -1px;
    line-height: 1;
  }
  .front-web {
    position: absolute;
    left: 0;
    right: 0;
    bottom: 34px;
    text-align: center;
    font-size: 15px;
    font-weight: 600;
    color: var(--paper);
  }
  .card-back {
    left: 550px;
    top: 480px;
    background: linear-gradient(135deg, var(--card-white) 0%, var(--paper) 45%, var(--card-white-shade) 100%);
  }
  .swoosh {
    position: absolute;
    left: 0;
    top: 0;
  }
  .brand {
    position: absolute;
    left: 44px;
    top: 40px;
  }
  .brand-name {
    font-size: 40px;
    font-weight: 700;
    color: var(--ink);
    line-height: 1;
  }
  .brand-tagline {
    margin-top: 6px;
    margin-left: 70px;
    font-size: 8px;
    font-weight: 700;
    letter-spacing: 0.5px;
    color: var(--ink);
  }
  .person {
    position: absolute;
    right: 40px;
    top: 170px;
    text-align: right;
    color: var(--ink);
  }
  .person-name {
    font-size: 21px;
    font-weight: 400;
    line-height: 1.1;
  }
  .person-title {
    font-size: 12px;
    font-weight: 600;
  }
  .contact {
    position: absolute;
    left: 44px;
    bottom: 34px;
    list-style: none;
    color: var(--ink);
    font-size: 13px;
    line-height: 1.2;
  }
  .contact li {
    display: flex;
    align-items: flex-start;
    gap: 10px;
    margin-top: 7px;
  }
  .contact svg {
    flex: none;
    width: 13px;
    height: 13px;
    margin-top: 2px;
    fill: var(--ink);
  }
</style>
</head>
<body>
<main class="canvas">

  <section class="card card-front" aria-label="Card front">
    <div class="front-name">Movrette</div>
    <div class="front-web">www.movrette.com</div>
  </section>

  <section class="card card-back" aria-label="Card back">
    <svg class="swoosh" width="540" height="310" viewBox="0 0 540 310" aria-hidden="true">
      <path d="M560 145 C 420 150 300 175 265 215 C 245 240 300 262 400 262 C 460 262 520 250 560 238 L 560 218 C 510 232 450 240 400 238 C 320 236 290 222 300 208 C 325 182 430 168 560 168 Z" fill="var(--swoosh)"/>
      <path d="M560 160 C 440 165 330 185 300 208 C 330 186 440 172 560 172 Z" fill="var(--swoosh-light)"/>
    </svg>

    <div class="brand">
      <div class="brand-name">Movrette</div>
      <div class="brand-tagline">PATRONS - PATTERNS</div>
    </div>

    <div class="person">
      <div class="person-name">Odile Parmont</div>
      <div class="person-title">president | présidente</div>
    </div>

    <ul class="contact">
      <li>
        <svg viewBox="0 0 16 16" aria-hidden="true"><path d="M1 3h14v10H1z M2 4.2v0.6l6 4.2 6-4.2V4.2z" fill-rule="evenodd"/></svg>
        <span>info@movrette.com</span>
      </li>
      <li>
        <svg viewBox="0 0 16 16" aria-hidden="true"><path d="M8 0C4.7 0 2.5 2.4 2.5 5.4 2.5 9.4 8 16 8 16s5.5-6.6 5.5-10.6C13.5 2.4 11.3 0 8 0zm0 7.6a2.2 2.2 0 1 1 0-4.4 2.2 2.2 0 0 1 0 4.4z"/></svg>
        <span>3915 rue Lavoie<br>St-Aubrevin QC H2K4P8</span>
      </li>
      <li>
        <svg viewBox="0 0 16 16" aria-hidden="true"><circle cx="8" cy="8" r="8"/><path d="M6 4.5c-.6.8-.9 2-.6 3.2.4 1.6 1.6 3 3 3.6.8.3 1.6.3 2.1 0l-.9-1.5c-.4.2-.9.1-1.3-.2-.7-.6-1.1-1.5-1.1-2.4 0-.4.2-.7.5-.9z" fill="var(--paper)"/></svg>
        <span>418-555-0187</span>
      </li>
    </ul>
  </section>

</main>
</body>
</html>
```